bramblecrest paving card makeover

were a excavation/paving contractor from Monterey ca, I'm looking to have a card designed front and back that has company details on the front and a list of the services we offer on the back.

Target Market(s)

home owners property management companies

Industry/Entity Type

Contractor

Contact Information for Business Card

bramblecrest paving 418 larkmoor st Monterey ca. licensed, insured and bonded
lic#657920 gerald pinsky operations manager

Font styles to use
Serif
Sans Serif

Colors
f78f20

Requirements
Must have
• a list of my services on back, asphalt construction and maintenance, drainage, foundations, retaining walls, chip seals, excavation, grading, landscape ground work, interlocking paver, hydro-seeding, structured and driveway demolition, utility trenching and stump removal.
Nice to have
• my new domain and page address I'm acquiring from pixel bazaar.

```html
<!DOCTYPE html>
<html lang="en">
<head>
<meta charset="utf-8">
<title>Bramblecrest Paving – Business Card</title>
<link href="https://fonts.googleapis.com/css2?family=Roboto+Condensed:wght@400;500;700&family=Roboto:wght@400;500&display=swap" rel="stylesheet">
<style>
  :root {
    --backdrop: #6e5240;
    --card: #1d1e20;
    --ink: #f2f2f2;
    --muted: #a9a9a9;
    --rule: #4a4b4d;
    --bullet: #9a9a9a;
  }
  html, body {
    margin: 0;
    width: 1200px;
    height: 960px;
    overflow: hidden;
    background: var(--backdrop);
  }
  .stage { position: relative; width: 1200px; height: 960px; }
  .card {
    position: absolute;
    width: 600px;
    height: 342px;
    background: var(--card);
    border-radius: 18px;
    box-shadow: 0 4px 10px rgba(0,0,0,.45);
    color: var(--ink);
    font-family: "Roboto", Arial, sans-serif;
  }
  .card--front { left: 302px; top: 125px; }
  .card--back { left: 300px; top: 493px; }

  .brand-mark {
    position: absolute;
    width: 210px;
    height: 210px;
    border: 3px solid var(--ink);
    border-radius: 50%;
    box-sizing: border-box;
    display: flex;
    align-items: center;
    justify-content: center;
    text-align: center;
    font-family: "Roboto Condensed", Arial, sans-serif;
    font-weight: 700;
    font-size: 25px;
    line-height: 1.1;
    letter-spacing: 1px;
    text-transform: uppercase;
    color: var(--ink);
  }
  .card--front .brand-mark { left: 58px; top: 66px; }
  .card--back .brand-mark { left: 215px; top: 52px; width: 170px; height: 170px; font-size: 20px; }

  .divider {
    position: absolute;
    left: 304px;
    top: 60px;
    width: 1px;
    height: 220px;
    background: var(--rule);
  }
  .details {
    position: absolute;
    left: 336px;
    top: 62px;
    font-size: 15px;
    line-height: 19px;
  }
  .details .name {
    font-family: "Roboto Condensed", Arial, sans-serif;
    font-weight: 400;
    font-size: 24px;
    line-height: 26px;
    color: var(--muted);
    text-transform: uppercase;
    margin: 0;
  }
  .details .role {
    font-weight: 500;
    font-size: 15px;
    line-height: 18px;
    text-transform: uppercase;
    margin: 0 0 12px;
  }
  .details p { margin: 0; }
  .details .credentials {
    font-family: "Roboto Condensed", Arial, sans-serif;
    font-weight: 700;
    font-size: 14px;
    margin-top: 2px;
  }
  .contact { list-style: none; margin: 9px 0 0; padding: 0; }
  .contact li { display: flex; align-items: center; gap: 8px; }
  .contact svg { width: 13px; height: 13px; fill: var(--muted); }

  .services {
    position: absolute;
    left: 0;
    right: 0;
    top: 242px;
    text-align: center;
    font-family: "Roboto Condensed", Arial, sans-serif;
    font-size: 15px;
    line-height: 19px;
  }
  .services p { margin: 0; }
  .services .dot { color: var(--bullet); }
</style>
</head>
<body>
<main class="stage">
  <section class="card card--front">
    <div class="brand-mark">Bramblecrest<br>Paving</div>
    <div class="divider"></div>
    <div class="details">
      <h1 class="name">Gerald Pinsky</h1>
      <p class="role">Operations Manager</p>
      <p>bramblecrest paving</p>
      <p>418 larkmoor st</p>
      <p>Monterey ca.</p>
      <p class="credentials">Licensed, Insured &amp; bonded</p>
      <p>lic#657920</p>
      <ul class="contact">
        <li><svg viewBox="0 0 24 24"><path d="M6.6 10.8a15 15 0 0 0 6.6 6.6l2.2-2.2a1 1 0 0 1 1-.25 11.4 11.4 0 0 0 3.6.57 1 1 0 0 1 1 1V20a1 1 0 0 1-1 1A17 17 0 0 1 3 4a1 1 0 0 1 1-1h3.5a1 1 0 0 1 1 1c0 1.25.2 2.45.57 3.57a1 1 0 0 1-.25 1z"/></svg>831 555 0142</li>
        <li><svg viewBox="0 0 24 24"><path d="M2 5h20v14H2zm2 2v.5l8 5 8-5V7l-8 5z"/></svg>info@bramblecrestpaving.com</li>
        <li><svg viewBox="0 0 24 24"><circle cx="12" cy="12" r="10"/></svg>www.bramblecrestpaving.com</li>
      </ul>
    </div>
  </section>

  <section class="card card--back">
    <div class="brand-mark">Bramblecrest<br>Paving</div>
    <div class="services">
      <p>Asphalt construction &amp; maintenance <span class="dot">•</span> Drainage <span class="dot">•</span> Foundations</p>
      <p>Retaining walls <span class="dot">•</span> Chip seals <span class="dot">•</span> Excavation <span class="dot">•</span> Grading <span class="dot">•</span> Landscape ground work</p>
      <p>Interlocking paver <span class="dot">•</span> Hydro-seeding <span class="dot">•</span> Structured &amp; driveway demolition</p>
      <p>Utility trenching &amp; stump removal</p>
    </div>
  </section>
</main>
</body>
</html>
```